Velmo BUSINESS CARD

Design an attention-grabbing business cards. Draw inspiration from the provided logo file. Please use the same font style as in the logo.
the back side of the card is for accent/decoration.

Contact Information for Business Card

PLEASE USE PROVIDED BUSINESS CARD SAMPLE

Other font styles liked:
• LUMETTE

Colors
EB3D1F
EC4F4E
F09395
F8D3D4
FCEDEE

Requirements
Must have
• RED, BLACK COLORS, SOLID BACK COLOR
Nice to have
• MAKE IT FANCY

```html
<!DOCTYPE html>
<html lang="en">
<head>
<meta charset="utf-8">
<title>Velmo Business Card</title>
<link rel="stylesheet" href="https://fonts.googleapis.com/css2?family=Orbitron:wght@500;700;800&family=Exo+2:wght@400&display=swap">
<style>
  :root {
    --backdrop: #989d99;
    --paper: #ffffff;
    --ink: #231f20;
    --brand-red: #dd2430;
    --pale-red: #f8d3d4;
    --white: #ffffff;
  }
  * { margin: 0; padding: 0; box-sizing: border-box; }
  html, body {
    width: 1200px; height: 1000px; overflow: hidden;
    background: var(--backdrop);
  }
  .canvas { position: relative; width: 1200px; height: 1000px; }
  .card {
    position: absolute; left: 267px; width: 665px; height: 383px; overflow: hidden;
  }
  .card--front { top: 73px; background: var(--paper); }
  .card--back { top: 501px; background: var(--brand-red); }

  .brand { position: absolute; left: 83px; top: 158px; width: 500px; height: 110px; }
  .brand__mark {
    position: absolute; left: 0; top: 0; width: 96px; height: 96px; background: var(--ink);
  }
  .brand__name {
    position: absolute; left: 108px; top: -3px;
    font-family: "Orbitron", sans-serif; font-weight: 700;
    font-size: 84px; line-height: 84px; letter-spacing: 4px; color: var(--ink);
    white-space: nowrap;
  }
  .brand__tagline {
    position: absolute; left: 116px; top: 80px;
    font-family: "Exo 2", sans-serif; font-weight: 400;
    font-size: 16px; line-height: 18px; letter-spacing: 0.8px; color: var(--ink); white-space: nowrap;
  }

  .contact {
    position: absolute; left: 30px; top: 0; color: var(--white);
    font-family: "Orbitron", sans-serif; white-space: nowrap;
  }
  .contact__name { position: absolute; top: 57px; font-size: 21px; font-weight: 800; letter-spacing: 1.5px; }
  .contact__role { position: absolute; top: 84px; font-size: 11px; font-weight: 500; letter-spacing: 8.5px; }
  .contact__email { position: absolute; top: 102px; font-size: 11px; font-weight: 500; letter-spacing: 2.4px; }
  .contact__phone {
    position: absolute; left: 0; font-size: 20px; font-weight: 800; letter-spacing: 1px;
    display: flex; align-items: center; gap: 10px;
  }
  .contact__phone svg { width: 22px; height: 22px; }
  .contact__phone--office { top: 178px; }
  .contact__phone--mobile { top: 204px; }
  .contact__address { position: absolute; top: 275px; font-size: 15px; font-weight: 500; letter-spacing: 1.8px; line-height: 19px; }
  .contact__web { position: absolute; top: 333px; font-size: 15px; font-weight: 500; letter-spacing: 1.8px; }

  .back-emblem {
    position: absolute; left: 320px; top: -16px; width: 420px; height: 420px;
    border-radius: 50%;
    background: radial-gradient(circle at 45% 50%, var(--pale-red) 0%, var(--white) 70%);
  }
</style>
</head>
<body>
<main class="canvas">
  <section class="card card--front" aria-label="Card front">
    <div class="brand">
      <div class="brand__mark"></div>
      <div class="brand__name">VELMO</div>
      <div class="brand__tagline">A FRESH TAKE ON 3PL</div>
    </div>
  </section>

  <section class="card card--back" aria-label="Card back">
    <div class="back-emblem" role="img" aria-label="Large decorative brand emblem in white and red"></div>
    <div class="contact">
      <div class="contact__name">ELENA BROOKS</div>
      <div class="contact__role">PRESIDENT</div>
      <div class="contact__email">EBROOKS@VELMO-LLC.COM</div>
      <div class="contact__phone contact__phone--office">
        <svg viewBox="0 0 24 24" aria-hidden="true"><path fill="#fff" d="M2 9c0-3 4-5 10-5s10 2 10 5v2h-5V9c0-1-2-1.5-5-1.5S7 8 7 9v2H2z"/><path fill="#fff" d="M6 12h12l2 8H4z"/><circle cx="12" cy="16" r="2" fill="#dd2430"/></svg>
        555-204-7781
      </div>
      <div class="contact__phone contact__phone--mobile">
        <svg viewBox="0 0 24 24" aria-hidden="true"><rect x="7" y="2" width="10" height="20" rx="2" fill="none" stroke="#fff" stroke-width="2"/><circle cx="12" cy="18.5" r="1" fill="#fff"/></svg>
        555-318-6642
      </div>
      <div class="contact__address">1480 N. 250 EAST<br>HARBOR VALE, IN, 46001</div>
      <div class="contact__web">VELMO-LLC.COM</div>
    </div>
  </section>
</main>
</body>
</html>
```